Business card design needed

My company does everything from wiring up your exisiting entertainment system, to installing a complete new system for you. We can mount your plasma on the wall, install an aerial point for you, setup some surround sound in your outdoor area or install a new cinema room in your house. Any Audio or Visual requirements you may have we can provide these for you. If you want to have a party to remember at your place or just some chilled sounds by the pool, we can give you just the right size system.

Industry/Entity Type

Entertainment

Contact Information for Business Card

The Sound Crew
Declan Whitford
e| declan@thesoundcrewqz.com.au
w| www.thesoundcrewqz.com.au
m| 0412 576 018

Requirements
Must have
• The logo that i have uploaded is just a starter...something similar to this but not exact or any new suggestions you have would be great too. Colour choice we are pretty easy on we did think Red and Yellow but happy to take advice, something that stands out from the rest i guess.

```html
<!DOCTYPE html>
<html lang="en">
<head>
<meta charset="utf-8">
<title>The Sound Crew – Business Card</title>
<link rel="stylesheet" href="https://fonts.googleapis.com/css2?family=Archivo:wght@400;800&display=swap">
<style>
  :root {
    --page: #ffffff;
    --card: #ffffff;
    --card-edge: #222222;
    --brand-red: #ee2e35;
    --brand-yellow: #fff78a;
    --brand-pink: #f8b4b6;
    --ink-dark: #58585a;
    --ink-grey: #8a8a8c;
  }
  * { margin: 0; padding: 0; box-sizing: border-box; }
  html, body {
    width: 1200px; height: 1000px; overflow: hidden;
    background: var(--page);
    font-family: "Archivo", Arial, sans-serif;
  }
  .card {
    position: absolute; left: 41px; top: 119px;
    width: 1062px; height: 613px;
    background: var(--card);
    border: 1px solid var(--card-edge);
    overflow: hidden;
  }
  .block { position: absolute; }
  .block--yellow { left: 503px; top: 38px; width: 293px; height: 267px; background: var(--brand-yellow); }
  .block--red { left: 607px; top: 115px; width: 455px; height: 498px; background: var(--brand-red); overflow: hidden; }
  .brand {
    position: absolute; left: 58px; top: 64px;
    color: var(--brand-red); font-weight: 800;
    font-size: 52px; line-height: 1.05; letter-spacing: -1px;
    white-space: nowrap;
  }
  .brand__mark {
    position: absolute; left: 148px; top: 149px;
    width: 171px; height: 94px; background: var(--brand-yellow);
  }
  .brand-large {
    position: absolute; left: 22px; top: 165px;
    color: var(--brand-pink); font-weight: 800;
    line-height: 0.9; letter-spacing: -3px; white-space: nowrap;
  }
  .brand-large__top { display: block; font-size: 84px; }
  .brand-large__bottom { display: block; font-size: 150px; margin-top: 20px; }
  .holder-name {
    position: absolute; left: 68px; top: 252px;
    font-size: 44px; font-weight: 800; letter-spacing: 2px;
    color: var(--ink-dark); white-space: nowrap;
  }
  .contact { position: absolute; left: 68px; top: 392px; list-style: none; }
  .contact__row {
    height: 66px; font-size: 31px; color: var(--ink-grey); white-space: nowrap;
  }
  .contact__label { font-weight: 800; color: var(--ink-dark); margin-right: 6px; }
</style>
</head>
<body>
  <div class="card">
    <div class="block block--yellow"></div>
    <div class="block block--red">
      <div class="brand-large" aria-hidden="true">
        <span class="brand-large__top">The Sound</span>
        <span class="brand-large__bottom">Crew</span>
      </div>
    </div>

    <div class="brand__mark"></div>
    <div class="brand">The Sound<br>Crew</div>

    <div class="holder-name">Declan Whitford</div>

    <ul class="contact">
      <li class="contact__row"><span class="contact__label">e|</span>declan@thesoundcrewqz.com.au</li>
      <li class="contact__row"><span class="contact__label">w|</span>www.thesoundcrewqz.com.au</li>
      <li class="contact__row"><span class="contact__label">m|</span>0412 576 018</li>
    </ul>
  </div>
</body>
</html>
```